Rtvlegal.com needs a wedsite. Law Office of Bernard T. Whitfield

Bernard T. Whitfield is a criminal law firm that is 5 years old. We have already had all the content written and now just need the website designed. We also just finished our logo design using Pixel Harbor and would like it used in the design of the website.

Industry/Entity Type

Law Firm

Number of Pages Required

5+ page

Requirements
Must have
• I was our new logo to be on the website also. I want Dallas sites as the stock pictures for the website. For example the Grey Stone Hall. I also need to be able to add ClipNest videos. It has to adjust to be seen on computers and also cell phones. I need to be able to have a information sheet for clients to fill out and submit back to me.

```html
<!DOCTYPE html>
<html lang="en">
<head>
<meta charset="utf-8">
<title>Law Office of Bernard T. Whitfield</title>
<link href="https://fonts.googleapis.com/css2?family=Cinzel:wght@400;600&family=Open+Sans:wght@400;600&display=swap" rel="stylesheet">
<style>
:root{
  --navy:#0b2a66;
  --navy-deep:#06183f;
  --navy-mid:#123a80;
  --gold:#a0620e;
  --link:#0b2a66;
  --page:#e9e9e9;
  --box:#ebebeb;
  --box-line:#d2d2d2;
  --text:#333;
  --cream:#f1d9a5;
}
*{box-sizing:border-box;margin:0;padding:0}
html,body{width:1155px;height:1200px;overflow:hidden}
body{position:relative;background:var(--page);font-family:"Open Sans",Arial,sans-serif;color:var(--text)}
.site-header{position:absolute;left:0;top:0;width:1155px;height:89px;background:linear-gradient(var(--navy-deep),var(--navy));border-bottom:4px solid #d9d9d9;z-index:3}
.brand{position:absolute;left:186px;top:6px;width:120px;height:120px;border-radius:50%;background:var(--navy);border:4px solid #dfe6f2;box-shadow:0 0 0 3px var(--navy-deep);display:flex;align-items:center;justify-content:center;text-align:center;z-index:4}
.brand span{font-family:"Cinzel",serif;font-weight:600;font-size:12px;line-height:1.3;color:#fff;padding:0 14px}
.main-nav{position:absolute;left:320px;top:14px;display:flex}
.nav-item{display:flex;flex-direction:column;padding:0 14px;border-right:1px solid #2a4f93;height:62px;font-family:"Cinzel",serif;font-size:12.5px;line-height:15px;color:#fff;text-transform:uppercase;letter-spacing:.4px}
.nav-item:last-child{border-right:0}
.nav-item svg{width:28px;height:28px;margin-bottom:6px}
.hero{position:absolute;left:0;top:100px;width:1155px;height:402px;background:radial-gradient(ellipse at 30% 50%,#7d7d7d,#3a3a3a 70%),#444}
.hero-copy{position:absolute;left:574px;top:108px;color:#fff}
.hero-copy h1{font-family:"Cinzel",serif;font-weight:400;font-size:21px;line-height:24px}
.hero-copy p{font-size:11px;line-height:14px;margin-top:6px;width:360px}
.hero-copy .call{font-size:15px;font-weight:600;margin-top:9px}
.hero-copy .call a{color:var(--cream)}
.content{position:absolute;left:165px;top:487px;width:825px;height:530px;background:#fff;z-index:2}
.intro{margin:8px 9px 0;background:var(--box);border:1px solid var(--box-line);height:118px;padding:14px 21px}
.intro h2,.team h2{font-family:"Cinzel",serif;font-weight:400;color:#333;font-size:22px;letter-spacing:.3px}
.intro p{font-size:11px;line-height:14px;margin-top:12px;color:#555}
.team h2{margin:35px 0 0 20px;font-size:21px}
.member{position:absolute;top:220px;width:230px;font-size:11.5px;line-height:14px;color:#222}
.member .face{width:82px;height:82px;border-radius:50%;background:radial-gradient(#e8d6bf,#cdb79c);margin:0 0 33px}
.member h3{font-family:Arial,sans-serif;font-size:13.5px;color:var(--gold);margin-top:7px}
.member a{font-family:Arial,sans-serif;font-size:9.5px;color:var(--link);text-decoration:none}
.site-footer{position:absolute;left:0;top:1004px;width:1155px;height:196px;background:linear-gradient(120deg,var(--navy-deep),var(--navy-mid) 60%,var(--navy-deep));color:#fff}
.footer-brand{position:absolute;left:183px;top:40px;width:90px;height:90px;border-radius:50%;background:var(--navy);border:3px solid #dfe6f2;display:flex;align-items:center;justify-content:center;text-align:center}
.footer-brand span{font-family:"Cinzel",serif;font-weight:600;font-size:9px;line-height:1.3;padding:0 10px}
.site-footer h4{font-family:"Cinzel",serif;font-weight:400;font-size:16px;padding-bottom:4px;border-bottom:1px solid #c9d2e4}
.quick{position:absolute;left:304px;top:36px;width:359px}
.quick ul{list-style:none;display:grid;grid-template-columns:231px 1fr;margin-top:8px;row-gap:6px}
.quick li{font-size:10px;line-height:14px;text-transform:uppercase}
.contact{position:absolute;left:720px;top:36px;width:270px}
.contact ul{list-style:none;margin-top:8px}
.contact li{display:flex;align-items:center;font-size:10.5px;height:24px}
.contact svg{width:13px;height:13px;margin-right:9px;fill:#fff}
</style>
</head>
<body>
<header class="site-header">
  <div class="brand"><span>Law Office of Bernard T. Whitfield</span></div>
  <nav class="main-nav">
    <div class="nav-item"><svg viewBox="0 0 28 28" fill="#fff"><circle cx="14" cy="8" r="6"/><path d="M3 28c0-8 5-12 11-12s11 4 11 12z"/></svg>Attorney<br>Profiles</div>
    <div class="nav-item"><svg viewBox="0 0 28 28" fill="none" stroke="#fff" stroke-width="2"><path d="M14 3v22M6 25h16M4 7h20M4 7l-3 9h6zM24 7l-3 9h6z"/></svg>How we<br>can help</div>
    <div class="nav-item"><svg viewBox="0 0 28 28" fill="#fff"><rect x="6" y="3" width="12" height="8" transform="rotate(40 12 7)"/><path d="M12 12l10 10-2 2-10-10z"/><rect x="2" y="24" width="14" height="3"/></svg>Case<br>Offenses</div>
    <div class="nav-item"><svg viewBox="0 0 28 28" fill="#fff"><path d="M14 2L2 8h24z"/><rect x="4" y="10" width="3" height="12"/><rect x="10" y="10" width="3" height="12"/><rect x="16" y="10" width="3" height="12"/><rect x="22" y="10" width="3" height="12"/><rect x="2" y="23" width="24" height="3"/></svg>Expungements &amp;<br>Non-Disclosures</div>
    <div class="nav-item"><svg viewBox="0 0 28 28" fill="none" stroke="#fff" stroke-width="2.5"><circle cx="9" cy="19" r="6"/><circle cx="20" cy="8" r="5"/><path d="M13 15l3-3"/></svg>Probations<br>&amp; Violations</div>
    <div class="nav-item"><svg viewBox="0 0 28 28" fill="#fff"><rect x="4" y="18" width="20" height="3"/><rect x="4" y="23" width="20" height="3"/><rect x="4" y="13" width="20" height="3"/><rect x="16" y="2" width="3" height="9"/><rect x="21" y="2" width="3" height="9"/></svg>DWI,<br>DUI</div>
  </nav>
</header>

<section class="hero" role="img" aria-label="Attorney in a grey suit holding a briefcase in a Dallas courtroom beside the scales of justice">
  <div class="hero-copy">
    <h1>Our Aggressive Criminal<br>Defense Team Fights for You</h1>
    <p>Our Dallas-Fort Worth law firm solely handles criminal defense cases so we can dedicate our full resources to the pursuit of justice.</p>
    <p class="call">Call the Law Office &nbsp;at 972.555.0148</p>
    <p class="call" style="margin-top:4px">or <a href="#">contact us online</a></p>
  </div>
</section>

<main class="content">
  <section class="intro">
    <h2>Our Dallas Attorneys Protect Your Rights to Justice</h2>
    <p>You have the right to remain silent and to have an attorney present for questioning. You should exercise these constitutional rights when charged with a serious crime. Do not say anything since even a seemingly innocent statement could lead to incriminating evidence and trying to talk your way out of it could have the opposite effect. Ask for a lawyer then call the Law Office of Bernard T. Whitfield for help.</p>
  </section>
  <section class="team">
    <h2>Meet Our Criminal Defense Team:</h2>
    <article class="member" style="left:37px">
      <div class="face" role="img" aria-label="Portrait of Kyle Ramsden" style="margin-left:93px"></div>
      <p>Vel illum dolore eu feugiat nulla facilisis at vero eros et accumsan et iusto dignissim qui blandit praesent lupt zril delenit augue duis dolore te feugait nulla facilisi.</p>
      <h3>Kyle Ramsden</h3><a href="#">read more +</a>
    </article>
    <article class="member" style="left:300px">
      <div class="face" role="img" aria-label="Portrait of Bernard T. Whitfield" style="margin-left:90px"></div>
      <p>Typi non habent claritatem insitam est us legentis in iis qui facit eorum claritatem. Investigationes demonstraverunt lectores legere me lius quod ii legunt saepius.</p>
      <h3>Bernard T. Whitfield</h3><a href="#">read more +</a>
    </article>
    <article class="member" style="left:572px">
      <div class="face" role="img" aria-label="Portrait of Nadia Hale-Grant" style="margin-left:63px"></div>
      <p>Claritas est etiam processus dynamicus sequitur mutationem consuetudium lectorum. Mirum est notare quam littera gothica, quam nunc pumus parum clam, anteposuerit litterarum formas.</p>
      <h3>Nadia Hale-Grant</h3><a href="#">read more +</a>
    </article>
  </section>
</main>

<footer class="site-footer">
  <div class="footer-brand"><span>Law Office of Bernard T. Whitfield</span></div>
  <nav class="quick">
    <h4>Quick Links</h4>
    <ul>
      <li>Attorney Profile</li><li>Early Probation Release</li>
      <li>How We Can Help</li><li>Probation Violations</li>
      <li>Murder &amp; Other Homicide Offenses</li><li>Other Violent Offenses</li>
      <li>Sexual Offenses</li><li>DWI, DUI</li>
      <li>Expungements &amp; Non-Disclosures</li><li>Drug Offenses</li>
    </ul>
  </nav>
  <address class="contact" style="font-style:normal">
    <h4>Contact Us</h4>
    <ul>
      <li><svg viewBox="0 0 14 14"><path d="M7 0a5 5 0 0 0-5 5c0 4 5 9 5 9s5-5 5-9a5 5 0 0 0-5-5zm0 7a2 2 0 1 1 0-4 2 2 0 0 1 0 4z"/></svg>41 Elm Street, Dallas, Texas, USA</li>
      <li><svg viewBox="0 0 14 14"><path d="M0 3h14v8H0zM1 4l6 4 6-4" stroke="#0b2a66" stroke-width="1"/></svg>contact@rtvlegal.com</li>
      <li><svg viewBox="0 0 14 14"><path d="M3 1l2 3-1 2c1 2 2 3 4 4l2-1 3 2-2 3C5 14 0 9 0 3z"/></svg>972.555.0148</li>
    </ul>
  </address>
</footer>
</body>
</html>
```